Flyer-Design für Wohungsvermietung
Zielgruppe
Ich vermiete in einer Neubausiedlung 'Rosenhang Feldbrück' Wohnungen und möchte gerne für die Erstvermietung einen Flyer erstellen lassen, welchen wir in der Region aushängen bzw. abgeben können.
Aufgabenstellung
Flyer sollte über das Format A5 verfügen und auf beiden Seiten bedruckbar sein. Die Grafik sollte ansprechend für alle Altergruppen sein. Auf den Ersten Blick sollten alle wichtige Informationen ersichtlich sein. Es handelt sich um hochwertige Mietwohnungen mit einer ausgezeichneten Aussicht auf die Alpen. Die Schule befindet sich gleich anschliessend an die neue Siedlung. Ausführliche Informationen gibt es bereits auf einer Webseite: https://www.rosenhang-feldbrueck-wohnen.ch

```html
<!DOCTYPE html>
<html lang="de">
<head>
<meta charset="utf-8">
<title>Rosenhang Feldbrück – Wohnungen</title>
<link href="https://fonts.googleapis.com/css2?family=Fira+Sans:wght@300;400&display=swap" rel="stylesheet">
<style>
  :root {
    --red: #b3282d;
    --ink: #1f1f1f;
    --paper: #ffffff;
    --map: #e9eee0;
    --sky: #8fb4dc;
    --meadow: #6f9a45;
  }
  * { margin: 0; padding: 0; box-sizing: border-box; }
  html, body { width: 849px; height: 1200px; overflow: hidden; background: var(--paper); }
  body { font-family: "Fira Sans", Arial, sans-serif; font-weight: 300; color: var(--ink); position: relative; }

  .brand { position: absolute; top: 100px; left: 0; width: 849px; text-align: center; }
  .brand-name { font-size: 42px; font-weight: 400; color: var(--red); letter-spacing: 2px; }

  .rule { position: absolute; left: 59px; width: 758px; height: 3px; background: var(--red); }
  .rule-top { top: 220px; }
  .rule-bottom { top: 1087px; }

  .tile { position: absolute; left: 59px; width: 308px; }
  .site-plan { top: 226px; height: 199px; background: linear-gradient(135deg, #e4ead9 0%, var(--map) 60%, #f2f4ee 100%); }
  .photo-street { top: 441px; height: 204px; background: linear-gradient(180deg, var(--sky) 0%, #c9dbe9 30%, var(--meadow) 55%, #8fae6a 100%); }
  .photo-houses { top: 661px; height: 205px; background: linear-gradient(180deg, #9dbfe2 0%, #dfe6ea 30%, #b9bcb4 55%, var(--meadow) 100%); }
  .photo-alps { top: 882px; height: 204px; background: linear-gradient(180deg, #a9c6e4 0%, #d6dde4 20%, #4f7a3c 45%, #8a9a5e 75%, #6f9a45 100%); }

  .copy { position: absolute; left: 385px; width: 430px; text-align: center; font-size: 16px; line-height: 22px; }
  .intro { top: 299px; }
  .facts { top: 447px; }
  .surroundings { top: 658px; }
  .surroundings .lead { margin-bottom: 25px; }
  .surroundings .list { line-height: 25px; }
  .closing { top: 927px; }
  .closing p { line-height: 23px; }
  .closing .groups { margin-top: 6px; }
  .closing .highlight { color: var(--red); }

  .footer { position: absolute; top: 1113px; left: 0; width: 849px; text-align: center; font-size: 16px; font-weight: 400; line-height: 26px; }
</style>
</head>
<body>
  <header class="brand">
    <span class="brand-name">Rosenhang Feldbrück</span>
  </header>

  <div class="rule rule-top"></div>

  <div class="tile site-plan" role="img" aria-label="Situationsplan der Siedlung mit den beiden Gebäuden"></div>

  <p class="copy intro">Die beiden Mehrfamilienhäuser bieten helle,<br>sonnige Wohnungen mit Ausrichtung gegen Süden.<br>Die beiden Gartenwohnungen zeichnet ein<br>abgeschlossener Wohngarten aus und von den<br>grosszügigen Attikawohnungen geniesst man den<br>ungehinderten Blick in die Alpen.</p>

  <div class="tile photo-street" role="img" aria-label="Luftaufnahme der Neubausiedlung entlang der Strasse"></div>
  <p class="copy facts">2 Gebäude zu 13 und 8 Wohnungen mit<br>2 ½ – 5 ½-Zimmern · grosse Balkone (11 m2)<br>Fernwärmeversorgung aus<br>zentraler Holzschnitzelheizung eigene<br>Waschmaschine / Tumbler in den<br>4 ½ und 5 ½-Zimmerwohnungen · hindernisfrei<br>mit Lift von der Einstellhalle erschlossen</p>

  <div class="tile photo-houses" role="img" aria-label="Luftaufnahme der Mehrfamilienhäuser mit Gärten"></div>
  <div class="copy surroundings">
    <p class="lead">In der näheren Umgebung finden sie:</p>
    <p class="list">Hauszugänge mit festen Belägen<br>hindernisfrei<br>Kinderspielplatz mit Geräten<br>Hartplatz als Spiel- und Begegnungsplatz<br>Rasenflächen Gebüsch Bäume<br>Gehwege ins Dorf und ins Schulhaus</p>
  </div>

  <div class="tile photo-alps" role="img" aria-label="Blick über das Dorf auf die Alpen"></div>
  <div class="copy closing">
    <p>Der Rosenhang bietet eine<br>lebendige Wohnumgebung für</p>
    <p class="groups"><span class="highlight">Familien, Paare, Singles und Senioren –</span></p>
    <p class="groups">im Rosenhang Feldbrück fühlen sich <span class="highlight">ALLE</span> wohl.</p>
  </div>

  <div class="rule rule-bottom"></div>

  <footer class="footer">
    Information und Verwaltung:<br>
    kl immobilien ag • Talackerstrasse 7 • CH- 3046 Feldbrück • info@kl-immo.ch • www.kl-immo.ch
  </footer>
</body>
</html>
```